Minimalist Professional Business Card Design

We will be revamping our marketing materials: Business cards, Website and Catalogs.
Our Overall Design direction is to have a Minimalist artwork with Professionalism and Premium feel. The revamp starts with the new business card design followed by the others. Thus the designer whom work is selected for this job will likely to follow through with the subsequent jobs.

Target Market(s)

Upscale

Industry/Entity Type

Manufacturing

Contact Information for Business Card

For the Business Cards, the following are required:
. Minimalist yet Professional and Premium Feel
. Background Colors: white and / or light pastel yellow and if needed to smoothen the yellow, the light grey can be incorporated. We are changing our corporate bright yellow to either one of the three alternatives:
1. Soylant yellow CMYK (1%, 0%, 52%, 3%)
2. Popcorn yellow CMYK (0%, 0%, 33%, 0%)
3. Papaya yellow CMYK (0%, 0%, 51%, 0%)

Information to be inputed in the business cards:

Name: Barlen Moritova
Position: Managing Director

Company's name: Vellomar Valves Pte. Ltd.
Address: 512 Halvick Lane #07-09B
Singapore 617302
Tel: (65) 6281 4096
Fax: (65) 6294 7118
Email: barlen@vellomarvalves-example.com
Website: www.vellomarvalves-example.com
Skype: Vellomar.Valves
Whatsapp/ Line/ Viber/ WeChat: (65) 9372 6081

Company's Logo
Company's Slogan
Two product photos placed side by side (if this gets into the way of the design, it is OK not to include them)

Font styles to use
Serif

Colors
ffffff

Requirements
Must have
• Minimalist
Should not have
• Messy, crowded, playful

```html
<!DOCTYPE html>
<html lang="en">
<head>
<meta charset="utf-8">
<title>Vellomar Valves — Business Card</title>
<link href="https://fonts.googleapis.com/css2?family=Work+Sans:wght@400;500;600&family=Roboto:wght@400;500&family=Oswald:wght@500&family=Dancing+Script:wght@600&display=swap" rel="stylesheet">
<style>
  :root {
    --backdrop: #1e1e1e;
    --card-front: #fff8b8;
    --card-back: #bcbdc0;
    --ink: #58585a;
    --ink-soft: #4e4e50;
    --rule: #6a6a6a;
    --dot-1: #2bb24c;
    --dot-2: #7b519d;
    --dot-3: #3acd2f;
    --dot-4: #4cbf3a;
    --steel-light: #f2f2f2;
    --steel-mid: #cfd0d2;
    --steel-dark: #9a9b9e;
  }
  * { box-sizing: border-box; margin: 0; padding: 0; }
  html, body { width: 1200px; height: 897px; overflow: hidden; }
  body { background: var(--backdrop); position: relative; font-family: "Work Sans", sans-serif; color: var(--ink); }

  .card { position: absolute; left: 326px; width: 543px; height: 310px; border-radius: 17px; overflow: hidden; }
  .card--front { top: 127px; background: var(--card-front); }
  .card--back { top: 474px; background: var(--card-back); }

  /* brand lockup */
  .brand { position: absolute; display: flex; align-items: center; }
  .brand__mark { width: 76px; height: 76px; border: 7px solid var(--ink); border-radius: 50%; flex: none; }
  .brand__name { font-family: "Oswald", sans-serif; font-weight: 500; color: var(--ink); line-height: 1; }
  .card--front .brand { top: 29px; right: 29px; gap: 16px; }
  .card--front .brand__name { font-size: 38px; letter-spacing: 0; }

  /* name block */
  .holder__bar { position: absolute; left: 0; top: 130px; width: 17px; height: 33px; background: var(--ink); }
  .holder__bar::after { content: ""; position: absolute; left: 20px; top: 0; width: 3px; height: 33px; background: var(--ink); }
  .holder__name { position: absolute; left: 30px; top: 126px; font-family: "Roboto", sans-serif; font-weight: 400; font-size: 22px; color: var(--ink); letter-spacing: 0.2px; }
  .holder__role { position: absolute; left: 30px; top: 152px; font-size: 14px; color: var(--ink); }
  .divider { position: absolute; left: 30px; top: 182px; width: 484px; height: 1.5px; background: var(--rule); }

  /* contact details */
  .contacts { position: absolute; left: 29px; top: 199px; list-style: none; font-size: 14px; line-height: 17.5px; color: var(--ink-soft); }
  .contacts li { display: flex; align-items: center; gap: 7px; }
  .contacts svg { width: 11px; height: 11px; flex: none; fill: var(--ink-soft); }
  .address { position: absolute; right: 29px; top: 199px; text-align: right; font-size: 14px; line-height: 17.5px; color: var(--ink-soft); font-style: normal; }
  .messaging { position: absolute; right: 29px; top: 269px; display: flex; align-items: center; gap: 5px; font-size: 14px; color: var(--ink-soft); }
  .messaging__dot { width: 14px; height: 14px; border-radius: 50%; }
  .messaging__dot:nth-child(1) { background: var(--dot-1); }
  .messaging__dot:nth-child(2) { background: var(--dot-2); }
  .messaging__dot:nth-child(3) { background: var(--dot-3); }
  .messaging__dot:nth-child(4) { background: var(--dot-4); margin-right: 8px; }

  /* back */
  .company { position: absolute; left: 29px; top: 32px; font-family: "Oswald", sans-serif; font-weight: 500; font-size: 21px; line-height: 1.2; letter-spacing: 0.8px; color: var(--ink); white-space: nowrap; }
  .card--back .brand { left: 30px; top: 96px; width: 214px; flex-direction: column; gap: 10px; }
  .card--back .brand__mark { width: 82px; height: 82px; border-width: 7px; }
  .card--back .brand__name { font-size: 44px; }
  .slogan { position: absolute; left: 30px; top: 259px; font-family: "Dancing Script", cursive; font-weight: 600; font-size: 19px; color: var(--ink); white-space: nowrap; }
  .product { position: absolute; top: 34px; height: 248px; border-radius: 6px 6px 4px 4px; background: linear-gradient(90deg, var(--steel-dark), var(--steel-light) 40%, var(--steel-mid) 75%, var(--steel-dark)); }
  .product--one { left: 346px; width: 60px; }
  .product--two { left: 444px; width: 62px; }
</style>
</head>
<body>

<section class="card card--front" aria-label="Business card front">
  <div class="brand">
    <span class="brand__mark"></span>
    <span class="brand__name">VELLOMAR</span>
  </div>

  <div class="holder__bar"></div>
  <h1 class="holder__name">BARLEN MORITOVA</h1>
  <p class="holder__role">Managing Director</p>
  <div class="divider"></div>

  <ul class="contacts">
    <li><svg viewBox="0 0 12 12"><path d="M2.5 0.5 L4.5 0.5 L5 3.2 L3.8 4.2 C4.4 5.8 6 7.4 7.8 8.2 L8.8 7 L11.5 7.5 L11.5 9.5 C11.5 10.8 10.5 11.6 9.2 11.4 C4.8 10.6 1.4 7.2 0.6 2.8 C0.4 1.5 1.2 0.5 2.5 0.5Z"/></svg>(65) 6281 4096</li>
    <li><svg viewBox="0 0 12 12"><rect x="3" y="0.5" width="6" height="3"/><rect x="0.5" y="4" width="11" height="5" rx="1"/><rect x="3" y="8" width="6" height="3.5"/></svg>(65) 6294 7118</li>
    <li><svg viewBox="0 0 12 12"><path d="M0.5 2 H11.5 V10 H0.5Z M1.5 3 V9 H10.5 V3 L6 6.4Z M2 3 L6 5.6 L10 3Z" fill-rule="evenodd"/></svg>barlen@vellomarvalves-example.com</li>
    <li><svg viewBox="0 0 12 12"><circle cx="6" cy="6" r="5.2" fill="none" stroke="#4e4e50" stroke-width="1"/><ellipse cx="6" cy="6" rx="2.2" ry="5.2" fill="none" stroke="#4e4e50" stroke-width="1"/><path d="M1 6 H11 M1.6 3.5 H10.4 M1.6 8.5 H10.4" stroke="#4e4e50" stroke-width="0.9"/></svg>www.vellomarvalves-example.com</li>
    <li><svg viewBox="0 0 12 12"><circle cx="6" cy="6" r="5.5"/></svg>Vellomar.Valves</li>
  </ul>

  <address class="address">512 Halvick Lane #07-09B<br>Singapore 617302</address>

  <div class="messaging">
    <span class="messaging__dot"></span>
    <span class="messaging__dot"></span>
    <span class="messaging__dot"></span>
    <span class="messaging__dot"></span>
    <span>(65) 9372 6081</span>
  </div>
</section>

<section class="card card--back" aria-label="Business card back">
  <h2 class="company">VELLOMAR VALVES PTE. LTD.</h2>
  <div class="brand">
    <span class="brand__mark"></span>
    <span class="brand__name">VELLOMAR</span>
  </div>
  <p class="slogan">Made With Pride&nbsp; | &nbsp;For Heavy Duty</p>
  <div class="product product--one" role="img" aria-label="Product photo: stainless steel multistage submersible pump"></div>
  <div class="product product--two" role="img" aria-label="Product photo: stainless steel submersible motor"></div>
</section>

</body>
</html>
```